Kiosk Coin Venture: Safe and Secure Cash Money

Front of card: LOGO

Back of card:
$$$ FREE ATM PLACEMENT $$$
BENIFITS OF HAVING AN ATM AT YOUR BUSINESS
FREE ATM and BTM (Bitcoin) installation, maintenance, and loading.
Lower card processing fees
Stimulate more traffic.
Ease of access for customers
Maintain customers inside location.
Higher tips and spending

Contact me for more information!
Name: Tobias Merlano
Phone: (512) 638-9071 - Call or Text
Email: Tobias@KioskCoin.example

Contact Information for Business Card

The card should be shape of the logo. Only the back will have all the contact and business details.

Requirements
Must have
• The logo itself will be one side, the card will be the shape of the logo. contact details on back side.

```html
<!DOCTYPE html>
<html lang="en">
<head>
<meta charset="utf-8">
<title>Kiosk Coin Venture – Free ATM Placement Card</title>
<link rel="stylesheet" href="https://fonts.googleapis.com/css2?family=Bebas+Neue&family=Montserrat:wght@500;600;800&display=swap">
<style>
  :root {
    --backdrop: #3b3b3b;
    --card-black: #1c1c1c;
    --ink: #1a1a1a;
    --silver-dark: #8e8e8e;
    --silver-mid: #c9c9c9;
    --silver-light: #ffffff;
    --gold-light: #fff2a0;
    --gold-mid: #e8c23c;
    --gold-dark: #b8861a;
    --item-text: #d9d9d9;
  }
  html, body {
    margin: 0;
    padding: 0;
    width: 1200px;
    height: 1200px;
    overflow: hidden;
    background: var(--backdrop);
  }
  .card {
    display: block;
    width: 1200px;
    height: 1200px;
  }
  .headline {
    font-family: "Montserrat", sans-serif;
    font-weight: 800;
    font-size: 43px;
    fill: var(--ink);
  }
  .benefits-heading, .call-to-action {
    font-family: "Bebas Neue", sans-serif;
    font-size: 32px;
    fill: url(#gold-text);
  }
  .benefit-item {
    font-family: "Bebas Neue", sans-serif;
    font-size: 33px;
    fill: var(--item-text);
  }
  .contact-name {
    font-family: "Montserrat", sans-serif;
    font-weight: 600;
    font-size: 41px;
    letter-spacing: 3px;
    fill: var(--ink);
  }
  .contact-note {
    font-family: "Montserrat", sans-serif;
    font-weight: 500;
    font-size: 23px;
    fill: var(--ink);
  }
  .contact-phone {
    font-family: "Montserrat", sans-serif;
    font-weight: 500;
    font-size: 38px;
    fill: var(--ink);
  }
  .contact-web {
    font-family: "Montserrat", sans-serif;
    font-weight: 500;
    font-size: 31px;
    fill: var(--ink);
  }
  .icon-disc { fill: var(--ink); }
  .icon-line { fill: none; stroke: var(--silver-light); stroke-width: 1.4; }
  .coin { fill: url(#gold-coin); stroke: var(--gold-dark); stroke-width: 1; }
</style>
</head>
<body>
<svg class="card" viewBox="0 0 1200 1200" xmlns="http://www.w3.org/2000/svg" role="img" aria-label="Shield-shaped business card for Kiosk Coin Venture">
  <defs>
    <linearGradient id="silver" x1="0" y1="0" x2="1" y2="0">
      <stop offset="0" stop-color="var(--silver-dark)"/>
      <stop offset="0.2" stop-color="var(--silver-mid)"/>
      <stop offset="0.5" stop-color="var(--silver-light)"/>
      <stop offset="0.72" stop-color="var(--silver-mid)"/>
      <stop offset="0.85" stop-color="var(--silver-light)"/>
      <stop offset="1" stop-color="var(--silver-dark)"/>
    </linearGradient>
    <linearGradient id="gold-text" x1="0" y1="0" x2="0" y2="1">
      <stop offset="0" stop-color="var(--gold-light)"/>
      <stop offset="0.55" stop-color="var(--gold-mid)"/>
      <stop offset="1" stop-color="var(--gold-dark)"/>
    </linearGradient>
    <radialGradient id="gold-coin" cx="0.4" cy="0.35" r="0.7">
      <stop offset="0" stop-color="var(--gold-light)"/>
      <stop offset="0.6" stop-color="var(--gold-mid)"/>
      <stop offset="1" stop-color="var(--gold-dark)"/>
    </radialGradient>
  </defs>

  <!-- shield frame -->
  <path class="shield-rim" fill="url(#silver)"
        d="M600,65 L950,177 L950,858 Q950,900 910,928 L600,1135 L290,928 Q250,900 250,858 L250,177 Z"/>
  <path class="shield-body" fill="var(--card-black)"
        d="M600,76 L940,185 L940,856 Q940,894 903,920 L600,1123 L297,920 Q260,894 260,856 L260,185 Z"/>

  <!-- header band -->
  <path class="header-band" fill="url(#silver)" d="M289,203 L601,102 L914,202 L914,290 L289,290 Z"/>
  <text class="headline" x="600" y="261" text-anchor="middle" textLength="545" lengthAdjust="spacingAndGlyphs">FREE ATM PLACEMENT</text>

  <!-- benefits -->
  <text class="benefits-heading" x="598" y="387" text-anchor="middle" textLength="508" lengthAdjust="spacingAndGlyphs">BENIFITS OF HAVING AN ATM AT YOUR BUSINESS:</text>

  <g class="benefit-list">
    <circle class="coin" cx="350" cy="449" r="15"/>
    <text class="benefit-item" x="376" y="446" textLength="483" lengthAdjust="spacingAndGlyphs">FREE ATM AND BTM (BITCOIN) INSTALLATION,</text>
    <text class="benefit-item" x="376" y="473" textLength="322" lengthAdjust="spacingAndGlyphs">MAINTENANCE, AND LOADING.</text>

    <circle class="coin" cx="350" cy="503" r="15"/>
    <text class="benefit-item" x="378" y="518" textLength="343" lengthAdjust="spacingAndGlyphs">LOWER CARD PROCESSING FEES.</text>

    <circle class="coin" cx="350" cy="550" r="15"/>
    <text class="benefit-item" x="378" y="565" textLength="287" lengthAdjust="spacingAndGlyphs">STIMULATE MORE TRAFFIC.</text>

    <circle class="coin" cx="350" cy="595" r="15"/>
    <text class="benefit-item" x="378" y="610" textLength="360" lengthAdjust="spacingAndGlyphs">EASE OF ACCESS FOR CUSTOMERS.</text>

    <circle class="coin" cx="350" cy="641" r="15"/>
    <text class="benefit-item" x="378" y="656" textLength="436" lengthAdjust="spacingAndGlyphs">MAINTAIN CUSTOMERS INSIDE LOCATION.</text>

    <circle class="coin" cx="350" cy="693" r="15"/>
    <text class="benefit-item" x="378" y="706" textLength="302" lengthAdjust="spacingAndGlyphs">HIGHER TIPS AND SPENDING.</text>
  </g>

  <text class="call-to-action" x="600" y="797" text-anchor="middle" textLength="438" lengthAdjust="spacingAndGlyphs">CONTACT ME FOR MORE INFORMATION!</text>

  <!-- contact panel -->
  <path class="contact-panel" fill="url(#silver)"
        d="M287,823 L912,823 L912,860 Q910,905 870,940 L600,1093 L330,940 Q290,905 288,860 Z"/>

  <text class="contact-name" x="600" y="875" text-anchor="middle" textLength="389" lengthAdjust="spacingAndGlyphs">TOBIAS MERLANO</text>
  <text class="contact-note" x="446" y="904">Call or Text</text>

  <g class="icon-phone">
    <circle class="icon-disc" cx="417" cy="927" r="17"/>
    <path fill="var(--silver-light)" d="M410,917 q3,-2 5,1 l2,4 q1,2 -1,3 l-1,1 q2,4 6,6 l1,-1 q1,-2 3,-1 l4,2 q3,2 1,5 l-2,2 q-3,2 -9,-2 q-7,-5 -10,-11 q-2,-5 1,-9 z"/>
  </g>
  <text class="contact-phone" x="442" y="939" textLength="293" lengthAdjust="spacingAndGlyphs">(512) 638-9071</text>

  <g class="icon-web">
    <circle class="icon-disc" cx="417" cy="970" r="16"/>
    <circle class="icon-line" cx="417" cy="970" r="9"/>
    <ellipse class="icon-line" cx="417" cy="970" rx="4" ry="9"/>
    <line class="icon-line" x1="408" y1="970" x2="426" y2="970"/>
    <line class="icon-line" x1="410" y1="965" x2="424" y2="965"/>
    <line class="icon-line" x1="410" y1="975" x2="424" y2="975"/>
  </g>
  <text class="contact-web" x="444" y="981" textLength="350" lengthAdjust="spacingAndGlyphs">www.KioskCoin.example</text>
</svg>
</body>
</html>
```